Road Construction Company needs business cards

We would like a new business card designed for our business.

We're a road construction company based in Qld, Australia.

Can the business card please have the following information on it.

Name: Brent Malvoy
Position: General Manager
Phone: 0471 592 304
Email: Brent.malvoy@quendix.com.au
Address: 87 Harrowgate Ave, Pindarra, QLD, 4000
Website: www.quendix.com.au

Visually we'd like the card to be professional and simple.

Attached is our logo.

Our website is www.quendix.com.au

Target Market(s)

Men aged 25-60

Contact Information for Business Card

As listed in project description

Font styles to use
Serif

Requirements
Must have
• Large logo on back of card

```html
<!DOCTYPE html>
<html lang="en">
<head>
<meta charset="utf-8">
<title>Quendix Business Card</title>
<link rel="stylesheet" href="https://fonts.googleapis.com/css2?family=Nunito+Sans:wght@400;600;800;900&display=swap">
<style>
  :root {
    --navy: #0d4489;
    --sky: #2fa5d9;
    --ink: #1b1f2a;
    --paper: #ffffff;
    --stage: #ffffff;
  }
  * { margin: 0; padding: 0; box-sizing: border-box; }
  html, body { width: 1045px; height: 1200px; overflow: hidden; background: var(--stage); }
  body { font-family: "Nunito Sans", Arial, sans-serif; color: var(--ink); }

  .card-set {
    position: absolute;
    top: 465px;
    left: 35px;
    display: flex;
    gap: 35px;
  }
  .card {
    position: relative;
    width: 470px;
    height: 270px;
    overflow: hidden;
    box-shadow: 0 6px 16px rgba(0,0,0,0.28);
  }

  /* Front */
  .card-front { background: var(--navy); }
  .card-front .front-band {
    position: absolute; left: 0; right: 0; bottom: 0; height: 54px;
    background: var(--sky);
  }
  .card-front .brand-name {
    position: absolute; left: 0; right: 0; top: 84px;
    text-align: center;
    font-weight: 900; font-size: 62px; letter-spacing: 1px;
    color: var(--paper);
  }

  /* Back */
  .card-back { background: var(--paper); }
  .card-back .brand-name {
    position: absolute; left: 38px; top: 24px;
    font-weight: 900; font-size: 32px; letter-spacing: 0.5px;
    color: var(--navy);
  }
  .name-band {
    position: absolute; left: 0; right: 0; top: 91px; height: 54px;
    background: var(--sky);
    padding: 9px 0 0 36px;
    color: var(--paper);
  }
  .name-band .person-name {
    font-weight: 800; font-size: 19px; letter-spacing: 1px; text-transform: uppercase;
    line-height: 1.1;
  }
  .name-band .person-role {
    font-weight: 600; font-size: 10.5px; letter-spacing: 0.8px; text-transform: uppercase;
  }
  .contact-list {
    position: absolute; left: 34px; top: 174px;
    list-style: none;
    font-size: 12.5px; line-height: 1;
  }
  .contact-list li {
    display: flex; align-items: center; gap: 12px;
    height: 21px;
  }
  .contact-list svg, .address svg { width: 11px; height: 11px; fill: var(--sky); flex: none; }
  .address {
    position: absolute; left: 264px; top: 174px;
    display: flex; gap: 11px;
    font-size: 13px; font-weight: 600; line-height: 1.45;
  }
  .address svg { width: 13px; height: 15px; margin-top: 2px; }
</style>
</head>
<body>
  <main class="card-set">
    <section class="card card-front" aria-label="Card front">
      <div class="brand-name">QUENDIX</div>
      <div class="front-band"></div>
    </section>

    <section class="card card-back" aria-label="Card back">
      <div class="brand-name">QUENDIX</div>
      <div class="name-band">
        <div class="person-name">Brent Malvoy</div>
        <div class="person-role">General Manager</div>
      </div>
      <ul class="contact-list">
        <li>
          <svg viewBox="0 0 24 24" aria-hidden="true"><path d="M6.6 10.8a15.1 15.1 0 0 0 6.6 6.6l2.2-2.2c.3-.3.7-.4 1-.2 1.1.4 2.3.6 3.6.6.6 0 1 .4 1 1V20c0 .6-.4 1-1 1C10.6 21 3 13.4 3 4c0-.6.4-1 1-1h3.5c.6 0 1 .4 1 1 0 1.3.2 2.5.6 3.6.1.3 0 .7-.2 1z"/></svg>
          <span>0471 592 304</span>
        </li>
        <li>
          <svg viewBox="0 0 24 24" aria-hidden="true"><path d="M2 5h20v3l-10 6L2 8z"/><path d="M2 10l10 6 10-6v9H2z"/></svg>
          <span>brent.malvoy@quendix.com.au</span>
        </li>
        <li>
          <svg viewBox="0 0 24 24" aria-hidden="true"><path d="M12 2a10 10 0 1 0 0 20 10 10 0 0 0 0-20zm6.9 6h-3a15.7 15.7 0 0 0-1.4-3.6A8 8 0 0 1 18.9 8zM12 4c.8 1.2 1.5 2.5 1.9 4h-3.8c.4-1.5 1.1-2.8 1.9-4zM4.3 14a8.2 8.2 0 0 1 0-4h3.4a16.5 16.5 0 0 0 0 4zm.8 2h3a15.7 15.7 0 0 0 1.4 3.6A8 8 0 0 1 5.1 16zm3-8h-3a8 8 0 0 1 4.4-3.6C8.9 5.5 8.4 6.7 8.1 8zM12 20c-.8-1.2-1.5-2.5-1.9-4h3.8c-.4 1.5-1.1 2.8-1.9 4zm2.3-6H9.7a14.7 14.7 0 0 1 0-4h4.6a14.7 14.7 0 0 1 0 4zm.2 5.6c.6-1.1 1.1-2.3 1.4-3.6h3a8 8 0 0 1-4.4 3.6zm1.8-5.6a16.5 16.5 0 0 0 0-4h3.4a8.2 8.2 0 0 1 0 4z"/></svg>
          <span>www.quendix.com.au</span>
        </li>
      </ul>
      <div class="address">
        <svg viewBox="0 0 24 28" aria-hidden="true"><path d="M12 0C5.4 0 0 5.2 0 11.6 0 20 12 28 12 28s12-8 12-16.4C24 5.2 18.6 0 12 0zm0 3a8.6 8.6 0 0 1 8.7 8.6c0 5.4-6.6 11.2-8.7 12.8-2.1-1.6-8.7-7.4-8.7-12.8A8.6 8.6 0 0 1 12 3zm0 4.6a4 4 0 1 0 0 8 4 4 0 0 0 0-8z"/></svg>
        <p>87 Harrowgate Ave,<br>Pindarra, QLD,<br>4000</p>
      </div>
    </section>
  </main>
</body>
</html>
```